Tarvimoor business cards

Need fresh design for our business cards. Logo must be specific, we are open for everything else.

Contact Information for Business Card

phrase "GMP & JANITORIAL SERVICES" should be used as main point of card

Colors
3176b5
3276b5
85acd3
cedeed
ffffff
0292cd
33a6d7
85cae6
cee9f5

Requirements
Must have
• The logo
Should not have
• crowded designs

```html
<!DOCTYPE html>
<html lang="en">
<head>
<meta charset="utf-8">
<title>Tarvimoor Business Cards</title>
<link href="https://fonts.googleapis.com/css2?family=Outfit:wght@400&family=Figtree:wght@600;700&display=swap" rel="stylesheet">
<style>
  :root {
    --brand-blue: #2d7dbd;
    --ink-white: #ffffff;
    --backdrop: #e8e8e8;
    --card-shadow: rgba(0, 0, 0, 0.18);
  }
  * { margin: 0; padding: 0; box-sizing: border-box; }
  html, body {
    width: 1200px;
    height: 800px;
    overflow: hidden;
    background: var(--backdrop);
  }
  .canvas {
    position: relative;
    width: 1200px;
    height: 800px;
  }
  .card {
    position: absolute;
    top: 278px;
    width: 419px;
    height: 240px;
    overflow: hidden;
    box-shadow: 0 12px 24px var(--card-shadow);
  }
  .card--front { left: 142px; background: var(--brand-blue); }
  .card--back { left: 637px; background: var(--brand-blue); }

  .front__header {
    position: absolute;
    left: 0; top: 0;
    width: 100%;
    height: 105px;
    background: var(--ink-white);
  }
  .brand-name {
    position: absolute;
    left: 29px;
    top: 32px;
    font-family: "Outfit", sans-serif;
    font-weight: 400;
    font-size: 47px;
    line-height: 1;
    letter-spacing: 10px;
    color: var(--brand-blue);
    white-space: nowrap;
  }

  .contact-list, .social-list {
    position: absolute;
    top: 135px;
    list-style: none;
    font-family: "Figtree", sans-serif;
    font-weight: 600;
    font-size: 15px;
    line-height: 18.5px;
    color: var(--ink-white);
  }
  .contact-list { left: 30px; }
  .social-list { left: 248px; font-size: 14px; }
  .contact-list li, .social-list li {
    display: flex;
    align-items: center;
    gap: 7px;
    white-space: nowrap;
  }
  .icon { width: 12px; height: 12px; flex: none; }
  .social-mark {
    width: 11px; height: 11px;
    background: var(--ink-white);
    flex: none;
    margin-right: 1px;
  }

  .tagline {
    position: absolute;
    left: 41px;
    top: 67px;
    font-family: "Figtree", sans-serif;
    font-weight: 700;
    font-size: 39px;
    line-height: 44px;
    color: var(--ink-white);
    letter-spacing: 0.2px;
    white-space: nowrap;
  }
</style>
</head>
<body>
<main class="canvas">
  <section class="card card--front" aria-label="Business card front">
    <header class="front__header">
      <div class="brand-name">TARVIMOOR</div>
    </header>
    <ul class="contact-list">
      <li>
        <svg class="icon" viewBox="0 0 12 12" aria-hidden="true"><rect width="12" height="12" rx="1.5" fill="#fff"/><path d="M3.2 2.6l1.3-.3.8 1.9-.9.7c.5 1 1.2 1.7 2.2 2.2l.7-.9 1.9.8-.3 1.3c-3.3 0-6-2.7-5.7-5.7z" fill="var(--brand-blue)"/></svg>
        1 (855) 410 7732
      </li>
      <li>
        <svg class="icon" viewBox="0 0 12 12" aria-hidden="true"><rect x="0" y="4" width="12" height="8" fill="#fff"/><rect x="3" y="0" width="6" height="5" fill="#fff"/><rect x="2" y="6" width="2" height="1.5" fill="var(--brand-blue)"/><rect x="5" y="6" width="2" height="1.5" fill="var(--brand-blue)"/><rect x="8" y="6" width="2" height="1.5" fill="var(--brand-blue)"/><rect x="2" y="9" width="2" height="1.5" fill="var(--brand-blue)"/><rect x="5" y="9" width="2" height="1.5" fill="var(--brand-blue)"/><rect x="8" y="9" width="2" height="1.5" fill="var(--brand-blue)"/></svg>
        (416) 552 0918
      </li>
      <li>
        <svg class="icon" viewBox="0 0 12 12" aria-hidden="true"><rect y="1.5" width="12" height="9" fill="#fff"/><path d="M1 3l5 3.5L11 3" stroke="var(--brand-blue)" stroke-width="1.3" fill="none"/></svg>
        INFO@TARVIMOOR.CA
      </li>
      <li>
        <svg class="icon" viewBox="0 0 12 12" aria-hidden="true"><rect width="12" height="12" fill="#fff"/><path d="M6 2.5L2 6h1.2v3.5h2.2V7.5h1.2v2h2.2V6H10z" fill="var(--brand-blue)"/></svg>
        WWW.TARVIMOOR.CA
      </li>
    </ul>
    <ul class="social-list">
      <li><span class="social-mark"></span>TARVIMOOR LTD.</li>
      <li><span class="social-mark"></span>TARVIMOOR</li>
    </ul>
  </section>

  <section class="card card--back" aria-label="Business card back">
    <p class="tagline">GMP &amp;<br>JANITORIAL<br>SERVICES</p>
  </section>
</main>
</body>
</html>
```